website re-design - the brickfern studio

The Brickfern Studio is an existing website that we built using a new zealand based online CMS tool which is quite flexible and accomodates custom designs. You can check it here: http://www.pagequilt.co.nz/.

We have a logo already and the content on the website is OK.
The website can be found at www.thebrickfernstudio.com.au

mainly the homepage, but if the design is easily adapted to the other pages then, we will commission the winner to update these pages also.
Updates

Hi there,  I am uploading an image to be used as the main image on the homepage design,  so all submissions have the same image.

Target Market(s)

property developers, architects, builders, home buyers

Industry/Entity Type

Shop

Requirements
Must have
• Must utilise the existing CMS or at least be compatible to upload
Nice to have
• a promotional banner that can be turned off and on and changed as required as we offer different promotions over time.

```html
<!DOCTYPE html>
<html lang="en">
<head>
<meta charset="utf-8">
<title>The Brickfern Studio – Architectural Scale Models</title>
<link href="https://fonts.googleapis.com/css2?family=Montserrat:wght@500;600;700&family=PT+Serif:ital@1&family=Arimo:wght@400;700&display=swap" rel="stylesheet">
<style>
:root{
  --orange:#e27a25;
  --orange-dark:#c8651a;
  --ink:#2b2b2b;
  --grey-text:#555;
  --muted:#7a7a7a;
  --line:#d9d9d9;
  --band:#f6f6f6;
  --tab-active:#666;
  --tweet-blue:#3d9fd3;
  --tweet-bg:#bfe6f7;
  --white:#fff;
}
*{margin:0;padding:0;box-sizing:border-box}
html,body{width:1200px;height:718px;overflow:hidden;background:var(--white);font-family:"Arimo",Arial,sans-serif;color:var(--ink)}
.page{position:relative;width:1200px;height:718px}
.abs{position:absolute}

.brand{left:189px;top:24px;display:flex;align-items:center;gap:12px}
.brand-mark{width:70px;height:46px;background:var(--orange)}
.brand-name{font-family:"Montserrat",sans-serif;font-weight:600;font-size:18px;color:var(--ink);line-height:1}
.brand-sub{font-family:"Montserrat",sans-serif;font-weight:600;font-size:8px;color:var(--orange);letter-spacing:.3px;margin-top:3px}

.phone{right:189px;top:19px;font-size:20px;color:#444}
.phone b{color:var(--orange)}
.search{left:770px;top:53px;width:241px;height:28px;border:1px solid var(--line);font-size:12px;color:#bbb;padding:7px 13px}
.search svg{position:absolute;right:8px;top:6px}

.hero-band{left:0;top:123px;width:1200px;height:333px;background:var(--band);border-top:1px solid #e4e4e4;border-bottom:1px solid #ddd}

.nav{left:189px;top:105px;height:36px;display:flex;border:1px solid var(--line);background:var(--white)}
.nav a{display:flex;align-items:center;justify-content:center;font-size:12.5px;color:var(--ink);text-decoration:none;border-left:1px solid var(--line);height:100%}
.nav a:first-child{border-left:none}
.nav .active{background:var(--tab-active);color:var(--white);font-weight:700}
.nav .quote{color:var(--orange)}

.headline{left:188px;top:198px;font-family:"Montserrat",sans-serif;font-weight:600;font-size:25px;line-height:26px;color:var(--ink)}
.headline span{color:var(--orange);font-weight:700}
.lede{left:190px;top:292px;width:320px;font-family:"PT Serif",Georgia,serif;font-style:italic;font-size:16px;line-height:18.5px;color:var(--muted)}
.read-more{left:190px;top:369px;width:173px;height:28px;background:linear-gradient(#ec8a3a,var(--orange-dark));color:var(--white);font-family:"Montserrat",sans-serif;font-weight:600;font-size:13.5px;display:flex;align-items:center;justify-content:center;box-shadow:0 2px 3px rgba(0,0,0,.25)}

.slide{left:543px;top:172px;width:468px;height:250px;background:linear-gradient(160deg,#9aa0a6 0%,#6d7a6a 45%,#b7b2ad 100%)}
.slide-arrow{top:272px;width:22px;height:35px;background:var(--white);border:1px solid var(--line);display:flex;align-items:center;justify-content:center}

.card{top:483px;width:263px;height:166px;border:1px solid var(--line);background:var(--white);box-shadow:0 1px 2px rgba(0,0,0,.08);padding:9px 8px;overflow:hidden}
.card h2{font-family:"Montserrat",sans-serif;font-weight:600;font-size:15.5px;color:var(--orange);padding-left:3px}
.card .pager{position:absolute;right:10px;top:16px}
.about h2{padding-bottom:7px;border-bottom:1px solid var(--line);margin-bottom:6px}
.about p{font-size:8.6px;line-height:15.5px;color:var(--grey-text);padding-left:1px}
.project-photo{margin-top:8px;height:118px;background:linear-gradient(180deg,#2f7fd0 0%,#6fb2ea 45%,#e8dcd0 46%,#d6c8bb 100%)}
.tweets h2{color:var(--tweet-blue)}
.tweet-panel{margin-top:8px;height:118px;background:var(--tweet-bg);padding:4px 6px;position:relative;overflow:hidden}
.tweet-bar{display:flex;gap:5px;padding-bottom:5px;border-bottom:1px solid #a9d6ea}
.chip{background:var(--white);border:1px solid #9cc7de;border-radius:2px;font-size:10px;font-weight:700;color:#2a6a95;padding:2px 5px}
.avatar{position:absolute;left:7px;top:40px;width:47px;height:43px;background:linear-gradient(#e9e4dc,#cfc3b2);border:2px solid var(--white)}
.byline{position:absolute;left:8px;top:87px;font-size:9.5px;color:#225a80}
.byline b{color:#1d4f73}
.bubble{position:absolute;left:67px;top:38px;width:170px;height:52px;border:2px solid #8fd0ee;border-radius:3px;background:#c9ecfb;font-size:8.4px;line-height:14px;color:#2c4d60;padding:4px 9px;white-space:nowrap}
.stamp{position:absolute;right:12px;top:99px;font-size:8px;color:#3a8bb8}

.footer{left:0;top:680px;width:1200px;height:38px;background:var(--band);border-top:1px solid var(--line);font-size:9.5px;color:#333}
.footer nav{position:absolute;left:189px;top:12px;display:flex;gap:20px}
.footer nav span{color:#666}
.footer .copy{position:absolute;right:189px;top:13px;font-size:9.3px}
</style>
</head>
<body>
<div class="page">
  <div class="hero-band abs"></div>

  <div class="brand abs">
    <div class="brand-mark"></div>
    <div>
      <div class="brand-name">THE BRICKFERN STUDIO</div>
      <div class="brand-sub">ARCHITECTURAL SCALE MODELS</div>
    </div>
  </div>

  <div class="phone abs"><b>PH:</b> (08) 6555 0148</div>
  <div class="search abs">Search
    <svg width="15" height="15" viewBox="0 0 15 15"><circle cx="6" cy="6" r="4.5" fill="none" stroke="#ccc" stroke-width="2"/><line x1="9.5" y1="9.5" x2="14" y2="14" stroke="#ccc" stroke-width="2.2"/></svg>
  </div>

  <nav class="nav abs">
    <a class="active" style="width:108px">Home</a>
    <a style="width:109px">Gallery</a>
    <a style="width:121px">Order Online</a>
    <a class="quote" style="width:121px">Get a Quote</a>
    <a style="width:121px">About us</a>
    <a style="width:121px">3D Visualisation</a>
    <a style="width:121px">Contact us</a>
  </nav>

  <h1 class="headline abs">A PICTURE’S WORTH A<br>THOUSAND WORDS...<br><span>A MODEL SAYS IT ALL...</span></h1>
  <p class="lede abs">If you answered yes to any of the following questions, then you should be using the brickfern studio.</p>
  <div class="read-more abs">READ MORE</div>

  <div class="slide abs" role="img" aria-label="Photo of an architectural scale model of a townhouse estate on a white table"></div>
  <div class="slide-arrow abs" style="left:531px"><svg width="8" height="12"><path d="M6 1L2 6l4 5" fill="none" stroke="#555" stroke-width="2"/></svg></div>
  <div class="slide-arrow abs" style="left:999px"><svg width="8" height="12"><path d="M2 1l4 5-4 5" fill="none" stroke="#111" stroke-width="2"/></svg></div>

  <section class="card about abs" style="left:189px">
    <h2>ABOUT US</h2>
    <p>The Brickfern Studio regards customer privacy as an important part of our relationship with our customers. The following privacy policy applies to all The Brickfern Studio users, and conforms to Internet privacy standards.<br>If you have questions or concerns regarding this statement, you should first contact Mara Ellison at admin@thebrickfernstudio.com.au.</p>
  </section>

  <section class="card abs" style="left:469px">
    <h2>OUR PROJECTS</h2>
    <svg class="pager" width="16" height="8"><path d="M4 0v8L0 4z M12 0v8l4-4z" fill="#555"/></svg>
    <div class="project-photo" role="img" aria-label="Photo of a white modern building with a red roof line against blue sky"></div>
  </section>

  <section class="card tweets abs" style="left:748px">
    <h2>NEWEST TWEETS</h2>
    <svg class="pager" width="16" height="8"><path d="M4 0v8L0 4z M12 0v8l4-4z" fill="#555"/></svg>
    <div class="tweet-panel">
      <div class="tweet-bar"><span class="chip">Tweet</span><span class="chip">7,231</span></div>
      <div class="avatar" role="img" aria-label="Profile photo of the tweet author"></div>
      <div class="byline">By:<b>Quillby</b></div>
      <div class="bubble">In the Harbourside area drive in<br>your vehicle to receive cash! Or<br>donate funds to your favorDrive it.</div>
      <div class="stamp">16 Hours Ago</div>
    </div>
  </section>

  <footer class="footer abs">
    <nav>Privacy Policy <span>|</span> Faq's <span>|</span> Sitemap <span>|</span> Contact us</nav>
    <div class="copy">© Copyright The Brickfern Studio - Site map, <b>Phone: (08) 6555 0148 Australia</b></div>
  </footer>
</div>
</body>
</html>
```